Looking for awesome business card design with attached existing logo

We are a water, mold, and fire damage restoration company called "Torvane Seco" Looking for an awesome business card that is edgy yet professional and unique. Show me what you got!

```html
<!DOCTYPE html>
<html lang="en">
<head>
<meta charset="utf-8">
<title>Torvane Seco — Business Card</title>
<link href="https://fonts.googleapis.com/css2?family=Lato:wght@400;700&family=Montserrat:wght@600;700&display=swap" rel="stylesheet">
<style>
  :root {
    --stage: #9a9a9a;
    --paper: #f4f4f3;
    --teal: #1d3f4b;
    --slate: #35515b;
    --gold: #d4971f;
    --red: #b8283a;
    --ink: #5a5a5a;
  }
  * { box-sizing: border-box; margin: 0; padding: 0; }
  html, body {
    width: 1200px; height: 976px; overflow: hidden;
    background: var(--stage);
  }
  .stage {
    position: relative; width: 1200px; height: 976px;
    display: flex; align-items: center; justify-content: center; gap: 70px;
  }
  .card {
    box-shadow: 0 3px 0 var(--gold), 0 18px 40px rgba(0,0,0,.25);
  }
  .card--front {
    width: 360px; height: 620px;
    background: var(--paper);
    padding: 70px 48px 0 56px;
    font-family: "Lato", sans-serif;
  }
  .front-brand {
    display: flex; align-items: center; gap: 12px;
    font-family: "Montserrat", sans-serif; font-weight: 700;
    font-size: 30px; color: var(--gold); letter-spacing: .5px;
  }
  .front-brand .dot {
    width: 14px; height: 14px; border-radius: 50%; background: var(--gold);
  }
  .person { margin-top: 96px; }
  .person-name {
    font-family: "Montserrat", sans-serif; font-weight: 700;
    font-size: 27px; color: var(--slate); letter-spacing: .3px;
  }
  .person-role {
    font-size: 17px; color: var(--gold); margin-top: 2px;
  }
  .rule {
    width: 18px; height: 2px; background: var(--red); margin: 22px 0 24px;
  }
  .address {
    font-size: 15px; color: var(--ink); line-height: 1.6;
  }
  .contacts {
    margin-top: 22px; list-style: none;
    font-size: 16px; color: var(--ink); line-height: 1.55;
  }
  .contacts li { display: flex; align-items: center; gap: 12px; }
  .contacts svg { width: 13px; height: 13px; flex: none; fill: var(--gold); }
  .card--back {
    width: 620px; height: 360px;
    background: var(--teal);
    display: flex; align-items: center; justify-content: center;
  }
  .back-brand {
    display: flex; align-items: center; gap: 18px;
    font-family: "Montserrat", sans-serif; font-weight: 700;
    font-size: 58px; color: var(--gold); letter-spacing: 1px;
  }
  .back-brand .dot {
    width: 22px; height: 22px; border-radius: 50%; background: var(--gold);
  }
</style>
</head>
<body>
<main class="stage">
  <section class="card card--front">
    <div class="front-brand"><span class="dot"></span>Torvane Seco</div>
    <div class="person">
      <h1 class="person-name">DANIEL HARWICK</h1>
      <p class="person-role">Founder &amp; CEO</p>
    </div>
    <div class="rule"></div>
    <p class="address">48 Harbor Lane, City<br>State, Zip 5021</p>
    <ul class="contacts">
      <li><svg viewBox="0 0 16 16"><path d="M3 1l3 3-1.5 2a9 9 0 0 0 5.5 5.5L12 10l3 3-2 2C7 15 1 9 1 3z"/></svg>(555) 214-3080</li>
      <li><svg viewBox="0 0 16 16"><path d="M4 0h8v16H4zM5.5 2v10h5V2z"/></svg>(555) 214-3081</li>
      <li><svg viewBox="0 0 16 16"><path d="M4 1h8v4H4zM1 6h14v7h-3v2H4v-2H1zM5 10v4h6v-4z"/></svg>(555) 214-3082</li>
      <li><svg viewBox="0 0 16 16"><path d="M1 3h14v10H1zM2.5 4.5L8 9l5.5-4.5z"/></svg>office@torvaneseco.com</li>
      <li><svg viewBox="0 0 16 16"><path d="M8 1a7 7 0 1 0 0 14A7 7 0 0 0 8 1zm0 2a5 5 0 0 1 4.9 4H3.1A5 5 0 0 1 8 3zm0 10a5 5 0 0 1-4.9-4h9.8A5 5 0 0 1 8 13z"/></svg>www.torvaneseco.com</li>
    </ul>
  </section>
  <section class="card card--back">
    <div class="back-brand"><span class="dot"></span>Torvane Seco</div>
  </section>
</main>
</body>
</html>
```